Drifting Marlo’s Coffee + Cannabis Packaging Design

Drifting Marlo's Coffee + Cannabis is a coffee shop dispensary in Albuquerque New Mexico. We need a packaging design for two bag sizes. 4'x5" and 3.4"x4". Our slogan is "Roasted + Toasted". We’re opening this year (2023) so a new company. Essentially I’d like the design to have the look of a National brand even though we’re a local New Mexico company. I don’t want anything super modern looking. There’s a back story you can find and read at www.driftingmarlosnm-example.com.

I’ve attached examples
Updates

A thought also that I really like, these will be 1g and 3.5G bags for cannabis. I like the idea of making them look like little coffee bags…

Target Market(s)

Persons 21-65

Industry/Entity Type

Cannabis + Coffee

Font styles to use
Other font styles liked:
• High Voltage Rough preferred but if the design is right I’d deviate

Colors

Designer to choose colors to be used in the design.

Requirements
Must have
• Drifting Marlo’s names a must. doesn’t have to have the logo. Just the same font.
Should not have
• Cartoon feels

```html
<!DOCTYPE html>
<html lang="en">
<head>
<meta charset="utf-8">
<title>Drifting Marlo’s Coffee + Cannabis — Bag Fronts</title>
<link rel="stylesheet" href="https://fonts.googleapis.com/css2?family=Oswald:wght@400;500;600&display=swap">
<style>
  :root {
    --stage: #161616;
    --bag: #1e1e1e;
    --bag-edge: #262626;
    --rust: #7a4a2a;
    --rust-light: #8d5a36;
    --ink-white: #ece9e4;
    --paper: #f4f2ee;
    --ink-black: #141414;
  }
  * { box-sizing: border-box; margin: 0; padding: 0; }
  html, body { width: 1200px; height: 1200px; overflow: hidden; }
  body {
    background: var(--stage);
    font-family: "Oswald", "Arial Narrow", sans-serif;
    color: var(--ink-white);
    position: relative;
  }
  .bag {
    position: absolute;
    top: 250px;
    width: 520px;
    height: 700px;
    background: linear-gradient(180deg, var(--bag-edge) 0%, var(--bag) 12%, var(--bag) 100%);
    border-radius: 6px;
  }
  .bag-front { left: 50px; }
  .bag-back { left: 630px; }

  /* Front label */
  .label-frame {
    position: absolute;
    left: 125px; top: 150px;
    width: 270px; height: 440px;
    border: 2px solid var(--rust);
  }
  .label-kicker {
    position: absolute; top: 18px; left: 0; right: 0;
    text-align: center;
    font-weight: 500; font-size: 17px; letter-spacing: 1.5px;
  }
  .brand-lockup {
    position: absolute; top: 62px; left: 0; right: 0;
    display: flex; flex-direction: column; align-items: center; gap: 12px;
  }
  .brand-dot {
    width: 34px; height: 34px; border-radius: 50%;
    background: var(--rust);
  }
  .brand-name {
    font-weight: 600; font-size: 20px; line-height: 1.15;
    text-align: center; color: var(--ink-white);
  }
  .spec-table {
    position: absolute; left: 40px; top: 258px;
    width: 190px;
    border-collapse: collapse;
    font-weight: 500;
  }
  .spec-table th {
    background: var(--paper); color: var(--ink-black);
    font-size: 19px; font-weight: 500; letter-spacing: 0.5px;
    padding: 3px 0; border: 1.5px solid var(--paper);
  }
  .spec-table td {
    border: 1.5px solid var(--paper);
    font-size: 15px; padding: 9px 8px;
  }
  .spec-table .cell-right { text-align: right; }
  .label-origin {
    position: absolute; bottom: 8px; left: 0; right: 0;
    text-align: center; font-size: 12px; font-weight: 500; letter-spacing: 0.5px;
  }

  /* Back: legend story */
  .legend-art {
    position: absolute; left: 70px; top: 120px;
    width: 340px; height: 370px;
    background: radial-gradient(ellipse at 40% 35%, #cfcfcf 0%, #9a9a9a 45%, #5e5e5e 100%);
  }
  .back-brand {
    position: absolute; right: 60px; top: 110px;
    display: flex; align-items: center; gap: 8px;
  }
  .back-brand .brand-dot { width: 22px; height: 22px; }
  .back-brand .brand-name { font-size: 15px; text-align: left; }
  .legend-title {
    position: absolute; left: 120px; top: 448px;
    font-weight: 500; font-size: 38px; letter-spacing: 3px;
    color: var(--rust);
  }
  .legend-story {
    position: absolute; left: 70px; top: 512px;
    width: 330px;
    font-size: 10.5px; line-height: 1.6; letter-spacing: 0.2px;
    color: var(--rust-light);
  }
</style>
</head>
<body>
  <section class="bag bag-front">
    <div class="label-frame">
      <p class="label-kicker">ULTRA PREMIUM CANNABIS</p>
      <div class="brand-lockup">
        <span class="brand-dot"></span>
        <p class="brand-name">Drifting Marlo’s<br>Coffee + Cannabis</p>
      </div>
      <table class="spec-table">
        <tr><th colspan="2">Roasted + Toasted</th></tr>
        <tr><td>THC : 5%</td><td class="cell-right">CBD : 12%</td></tr>
        <tr><td>7.11.23</td><td class="cell-right">150g</td></tr>
      </table>
      <p class="label-origin">Albuquerque New Mexico</p>
    </div>
  </section>

  <section class="bag bag-back">
    <div class="legend-art" role="img" aria-label="Sketched portrait of the bearded founder in a plaid shirt holding a mug, standing in a cannabis field"></div>
    <div class="back-brand">
      <span class="brand-dot"></span>
      <p class="brand-name">Drifting Marlo’s<br>Coffee + Cannabis</p>
    </div>
    <h2 class="legend-title">The Legend</h2>
    <p class="legend-story">In the groovy atmosphere of the 1970s, nestled within the heart of a small, tight-knit town, a legend was quietly taking shape – the persona known as Drifting Marlo. With a soul that thrived on the thrill of blending contrasts, Marlo embarked on a journey that seamlessly intertwined his love for coffee and cannabis, leaving an indelible mark on the era.</p>
  </section>
</body>
</html>
```